Varnet Immigration _Cloud-based, boutique law firm serving clients worldwide in US Immigration Law

I need a website for my new US immigration law firm that will be based in Larkmoor, Northvale but serve clients worldwide to achieve their US immigration goals. This will be a boutique firm offering attentive and compassionate service to our corporate and individual clients. I'd like the site to be fresh, modern, sophisticated and easy to read.

I will need a home page, about/bio page, services page, and contact me page with a form so potential clients could email inquiries and also schedule consultations. I would also like a 'Book a Consultation' button on the home page (easily visible).

The longest website page is going to be the 'Services' tab, which I'd like to break down to services for Employers and services Individuals, with further sub-sets of services to each type of client. I envision images with short text that display longer text when hoovering over.

To start, I would have 3 subsets of services for Employers and 5 subsets of services for Individuals. I will need the ability to expand/edit these pages in Wix interface as we grow.

The site will need to be in English and in French.

I like the color blue and the final design should communicate the firm's core values: integrity and compassion. In other words, we do right, no matter what and are understanding to individual circumstances. I'd like the site to convey sophistication and accessibility. I don't like staged stock photos of people. Sites with a lot of stock photos of people feels unauthentic to me.

Logo draft is attached in jpeg. Navy and gold colors.
Example of 4 law firm sites I like below:
- https://www.quillmarklaw.example/
-https://www.zentrolaw.example/
-https://orbinappeals.example/
-https://www.kalvorlaw.example/

Target Market(s)

Small-medium sized businesses (10-999 employees) in US with foreign workforce; Foreign entrepreneurs wishing to implant in the US

Industry/Entity Type

Law

Font styles to use
Sans Serif

Colors

Designer to choose colors to be used in the design.

Requirements
Must have
• Great Home Page (Grabs attention with eye-catching images/text; Immediately establishes credibility; Provides an overview of services; Encourages visitor to take the next action.)
Nice to have
• Images of Montreal (where firm is based); Images of bridges (symbolizes progress, movement, connections)
Should not have
• Non-authentic photos: staged people at desks or pictures of court buildings.

```html
<!DOCTYPE html>
<html lang="en">
<head>
<meta charset="utf-8">
<title>Varnet Immigration</title>
<link href="https://fonts.googleapis.com/css2?family=Cinzel:wght@400;500;600;700&family=Montserrat:wght@400;500;600&family=Allura&display=swap" rel="stylesheet">
<style>
:root{
  --navy:#2c3656;
  --navy-deep:#1d2a4d;
  --slate:#3b4061;
  --gold:#a8996a;
  --gold-soft:#c4b07a;
  --paper:#f4f5f8;
  --ink:#4a4f63;
  --line:#b9bcc6;
  --white:#ffffff;
}
*{box-sizing:border-box;margin:0;padding:0}
html,body{width:1200px;height:3595px;overflow:hidden}
body{position:relative;font-family:"Montserrat",sans-serif;color:var(--ink);background:var(--white)}
.abs{position:absolute}

/* Hero */
.hero{left:0;top:0;width:1200px;height:707px;
  background:linear-gradient(180deg,#1f3264 0%,#4a5a86 30%,#a98a8e 52%,#d89a6a 60%,#6a5a55 72%,#3a3434 100%)}
.brand{display:flex;align-items:center;gap:16px}
.brand-dot{width:92px;height:92px;border-radius:50%;background:var(--gold);opacity:.9}
.brand-name{font-family:"Cinzel",serif;color:var(--gold-soft);font-size:31px;line-height:1.1;letter-spacing:4px;font-weight:400}
.brand-sub{font-family:"Cinzel",serif;color:var(--gold-soft);font-size:13px;letter-spacing:3px;margin-top:6px}
.topbar{right:112px;top:32px;color:#fff;font-size:16px;display:flex;gap:14px;align-items:center}
.topbar svg{vertical-align:-2px;margin-right:4px}
.nav{right:112px;top:74px;display:flex;gap:38px;font-size:16px;color:#fff}
.nav .active{color:var(--gold-soft)}
.hero-title{left:0;width:1200px;top:160px;text-align:center;color:#fff;font-family:"Cinzel",serif;font-size:62px;line-height:62px;font-weight:600}
.hero-lead{left:0;width:1200px;top:302px;text-align:center;color:#fff;font-size:24px;font-weight:500}
.btn-ghost{left:460px;top:363px;width:280px;height:64px;border:2px solid #fff;color:#fff;font-size:19px;font-weight:500;display:flex;align-items:center;justify-content:center}

/* About */
.about-band{left:798px;top:707px;width:402px;height:667px;background:var(--slate)}
.portrait{left:640px;top:765px;width:448px;height:551px;background:linear-gradient(180deg,#f3f3f3,#e4e3e1 60%,#3a3f52 100%)}
.script{left:1068px;top:1200px;transform:rotate(-90deg);transform-origin:left top;font-family:"Allura",cursive;font-size:96px;color:var(--gold);white-space:nowrap}
.about-name{left:112px;top:815px;font-family:"Cinzel",serif;font-size:42px;color:var(--navy);font-weight:600}
.about-text{left:112px;width:470px;font-size:15.5px;line-height:26px;color:#6a6e7e}
.btn-outline{left:112px;top:1194px;width:153px;height:59px;border:2px solid var(--gold);color:var(--gold);font-size:17px;font-weight:500;display:flex;align-items:center;justify-content:center}

/* Services */
.services{left:0;top:1374px;width:1200px;height:1162px;background:var(--paper)}
.section-title{left:0;width:1200px;text-align:center;font-family:"Cinzel",serif;font-size:43px;color:var(--navy);font-weight:600}
.group-label{font-size:26px;color:#3b4060;font-weight:500;background:var(--paper);padding:0 10px}
.bracket{border:2px solid var(--line)}
.svc{width:160px;height:160px;border-radius:50%;background:var(--navy)}
.svc.gold{background:var(--gold)}
.svc-label{width:240px;text-align:center;font-size:20px;color:#3b4060}
.svc-heading{left:0;width:1200px;text-align:center;font-size:27px;color:#3b4060;font-weight:400}
.svc-text{left:210px;width:780px;text-align:center;font-size:16px;line-height:25px;color:#5c6072}

/* Contact */
.contact{left:0;top:2536px;width:1200px;height:703px;background:linear-gradient(180deg,#33477a 0%,#2f4270 45%,#3a4a6c 80%,#4a5060 100%)}
.contact-title{left:0;width:1200px;top:2608px;text-align:center;font-family:"Cinzel",serif;font-size:46px;color:#fff;font-weight:500}
.field-label{font-size:16px;color:#fff}
.field-label span{color:#c9a9a0}
.field{background:#f6f6f6}
.btn-send{left:537px;top:3102px;width:126px;height:56px;background:var(--gold);color:#fff;font-size:19px;font-weight:500;display:flex;align-items:center;justify-content:center}

/* Footer */
.footer-brand .brand-dot{width:108px;height:108px}
.footer-brand .brand-name{font-size:36px;color:var(--gold)}
.footer-brand .brand-sub{font-size:15px;color:var(--gold)}
.foot-head{font-size:19px;color:#3b4060;font-weight:500}
.foot-link{font-size:16px;color:#4a4f63}
.foot-link svg{vertical-align:-2px;margin-right:8px}
.rule{left:112px;top:3507px;width:976px;height:1px;background:#c7c9d0}
.copy{left:112px;top:3535px;font-size:16px;color:#4a4f63}
.social{width:42px;height:42px;border-radius:50%;background:var(--slate)}
</style>
</head>
<body>

<div class="abs hero" role="img" aria-label="City skyline at sunset seen from above"></div>
<div class="abs brand" style="left:112px;top:21px">
  <div class="brand-dot"></div>
  <div>
    <div class="brand-name">VARNET<br>IMMIGRATION</div>
    <div class="brand-sub">CLAIRE VARNET, ATTORNEY</div>
  </div>
</div>
<div class="abs topbar">
  <span><svg width="14" height="14" viewBox="0 0 24 24" fill="#fff"><path d="M6.6 10.8a15.5 15.5 0 0 0 6.6 6.6l2.2-2.2a1 1 0 0 1 1-.25 11.4 11.4 0 0 0 3.6.6 1 1 0 0 1 1 1V20a1 1 0 0 1-1 1A17 17 0 0 1 3 4a1 1 0 0 1 1-1h3.5a1 1 0 0 1 1 1c0 1.25.2 2.45.6 3.6a1 1 0 0 1-.25 1z"/></svg>1 800 555 0142</span>
  <span>|</span>
  <span><svg width="15" height="13" viewBox="0 0 24 20" fill="#fff"><rect x="1" y="2" width="22" height="16" rx="2"/><path d="M2 3l10 8 10-8" stroke="#3a4b7a" stroke-width="2" fill="none"/></svg>info@varnetimmigration.example</span>
  <span style="margin-left:8px">Eng ▾</span>
</div>
<nav class="abs nav">
  <span class="active">Home</span><span>About</span><span>Services</span><span>Contact</span>
</nav>
<h1 class="abs hero-title">Lighting the Way Through<br>U.S. Immigration Law</h1>
<p class="abs hero-lead">Let's get started.</p>
<div class="abs btn-ghost">BOOK A CONSULTATION</div>

<div class="abs about-band"></div>
<div class="abs portrait" role="img" aria-label="Portrait of the attorney in a dark suit"></div>
<div class="abs script">Attorney</div>
<h2 class="abs about-name">CLAIRE VARNET</h2>
<p class="abs about-text" style="top:894px">Lorem ipsum dolor sit amet, consectetur adipiscing elit, sed do eiusmod tempor incididunt.</p>
<p class="abs about-text" style="top:971px">Awt labore et dolore ma gna aliqua. Ut enim ad midenim veniam, quis nostrud exercitation ullamco laboris nisi ut aliquip ex ea commodo consequat. Duis aute irure dolor in reprehenderit in voluptate velit esse cillum dolore eu fugiat nulla pariatur. Excepteur sint occaecat cupidatat non proident, sunt in culpa qui officia deserunt mollit anim id est laborum.</p>
<div class="abs btn-outline">READ MORE</div>

<div class="abs services"></div>
<h2 class="abs section-title" style="top:1441px">SERVICES</h2>

<div class="abs bracket" style="left:681px;top:1567px;width:407px;height:129px;border-left:none"></div>
<div class="abs group-label" style="left:519px;top:1548px">Employers</div>
<div class="abs svc" style="left:133px;top:1611px" role="img" aria-label="Worker compensation icon"></div>
<div class="abs svc gold" style="left:322px;top:1611px" role="img" aria-label="Labor union icon"></div>
<div class="abs svc" style="left:510px;top:1611px" role="img" aria-label="Employment law icon"></div>
<div class="abs svc-label" style="left:93px;top:1780px">Worker Compensation</div>
<div class="abs svc-label" style="left:282px;top:1780px">Labor Union</div>
<div class="abs svc-label" style="left:470px;top:1780px">Employment Law</div>
<h3 class="abs svc-heading" style="top:1848px">Labor Union</h3>
<p class="abs svc-text" style="top:1905px">Duis aute irure dolor in reprehenderit in voluptate velit esse cillum dolore eu fugiat nulla par iatur. sed quia non numquam eius modi tempora incidunt ut labore et dolore magnam aliqua m quaerat voluptatem xercitationem ullam corporis suscipit laboriosam.</p>

<div class="abs bracket" style="left:134px;top:2045px;width:407px;height:128px;border-right:none;border-bottom:none"></div>
<div class="abs bracket" style="left:134px;top:2171px;width:42px;height:0;border-width:2px 0 0 0"></div>
<div class="abs group-label" style="left:540px;top:2026px">Individuals</div>
<div class="abs svc gold" style="left:175px;top:2089px" role="img" aria-label="Complex litigation icon"></div>
<div class="abs svc" style="left:364px;top:2089px" role="img" aria-label="Insurance law icon"></div>
<div class="abs svc" style="left:552px;top:2089px" role="img" aria-label="Personal injury icon"></div>
<div class="abs svc" style="left:739px;top:2089px" role="img" aria-label="Civil litigation icon"></div>
<div class="abs svc" style="left:929px;top:2089px" role="img" aria-label="US immigration law icon"></div>
<div class="abs svc-label" style="left:135px;top:2262px">Complex Litigation</div>
<div class="abs svc-label" style="left:324px;top:2262px">Insurance Law</div>
<div class="abs svc-label" style="left:512px;top:2262px">Personal Injury</div>
<div class="abs svc-label" style="left:699px;top:2262px">Civil Litigation</div>
<div class="abs svc-label" style="left:889px;top:2262px">US immigration law</div>
<h3 class="abs svc-heading" style="top:2335px">Complex Litigation</h3>
<p class="abs svc-text" style="top:2390px">Duis aute irure dolor in reprehenderit in voluptate velit esse cillum dolore eu fugiat nulla par iatur. sed quia non numquam eius modi tempora incidunt ut labore et dolore magnam aliqua m quaerat voluptatem xercitationem ullam corporis suscipit laboriosam.</p>

<div class="abs contact" role="img" aria-label="Steel bridge over a river under a blue tint"></div>
<h2 class="abs contact-title">CONTACT US TODAY</h2>
<label class="abs field-label" style="left:223px;top:2698px">First Name <span>*</span></label>
<label class="abs field-label" style="left:608px;top:2698px">Last Name <span>*</span></label>
<div class="abs field" style="left:224px;top:2726px;width:366px;height:52px"></div>
<div class="abs field" style="left:610px;top:2726px;width:365px;height:52px"></div>
<label class="abs field-label" style="left:223px;top:2799px">Email Address <span>*</span></label>
<label class="abs field-label" style="left:608px;top:2799px">Phone Number <span>*</span></label>
<div class="abs field" style="left:224px;top:2828px;width:366px;height:51px"></div>
<div class="abs field" style="left:610px;top:2828px;width:365px;height:51px"></div>
<label class="abs field-label" style="left:223px;top:2901px">How can we help you? <span>*</span></label>
<div class="abs field" style="left:224px;top:2931px;width:752px;height:138px"></div>
<div class="abs btn-send">SEND</div>

<div class="abs brand footer-brand" style="left:112px;top:3306px">
  <div class="brand-dot"></div>
  <div>
    <div class="brand-name">VARNET<br>IMMIGRATION</div>
    <div class="brand-sub">CLAIRE VARNET, ATTORNEY</div>
  </div>
</div>
<div class="abs foot-head" style="left:643px;top:3305px">Quick Links</div>
<div class="abs foot-link" style="left:643px;top:3352px">Home</div>
<div class="abs foot-link" style="left:643px;top:3381px">About</div>
<div class="abs foot-link" style="left:643px;top:3410px">Services</div>
<div class="abs foot-link" style="left:643px;top:3440px">Contact</div>
<div class="abs foot-head" style="left:815px;top:3305px">Contact Information</div>
<div class="abs foot-link" style="left:815px;top:3352px"><svg width="10" height="14" viewBox="0 0 10 14"><path d="M5 0a5 5 0 0 0-5 5c0 3.5 5 9 5 9s5-5.5 5-9a5 5 0 0 0-5-5zm0 7a2 2 0 1 1 0-4 2 2 0 0 1 0 4z" fill="var(--gold)"/></svg>Larkmoor, Northvale</div>
<div class="abs foot-link" style="left:815px;top:3394px"><svg width="12" height="12" viewBox="0 0 24 24"><path d="M6.6 10.8a15.5 15.5 0 0 0 6.6 6.6l2.2-2.2a1 1 0 0 1 1-.25 11.4 11.4 0 0 0 3.6.6 1 1 0 0 1 1 1V20a1 1 0 0 1-1 1A17 17 0 0 1 3 4a1 1 0 0 1 1-1h3.5a1 1 0 0 1 1 1c0 1.25.2 2.45.6 3.6a1 1 0 0 1-.25 1z" fill="var(--gold)"/></svg>1 800 555 0142</div>
<div class="abs foot-link" style="left:815px;top:3436px"><svg width="14" height="12" viewBox="0 0 24 20"><rect x="1" y="2" width="22" height="16" rx="2" fill="var(--gold)"/><path d="M2 3l10 8 10-8" stroke="#fff" stroke-width="2" fill="none"/></svg>info@varnetimmigration.example</div>
<div class="abs rule"></div>
<div class="abs copy">© 2023, Varnet Immigration. All rights reserved.</div>
<div class="abs social" style="left:949px;top:3524px"></div>
<div class="abs social" style="left:997px;top:3524px"></div>
<div class="abs social" style="left:1046px;top:3524px"></div>

</body>
</html>
```